Modern Minimalistic Supplement Label

Opportunity for recurring projects with a growing company. We have provided a detailed creative brief and all necessary files and guidelines. If you have any questions we will be closely monitoring the discussion board and email provided.

THE NAMES LISTED IN THE BRIEF ARE DIFFERENT FROM THE LABEL TEMPLATES. This is a private label brand. The label templates given are generic so please examine the entire brief before starting.

Use the PSD mockups attached and pair the labels with the correct bottles.

Do not use an entirely white background.

This could be excellent portfolio material.

Start by looking at the "CREATIVE_BRIEF" file. Logo files are contained in the "67046451" zip file.

UPDATE* Use the following business address for the "manufactured for" box on the labels.

Bramwell
4817 Pelton Ave. #2096
Ann Arbor MI 48276

Target Market(s)

All information provided in "CREATIVE_BRIEF" file.

Industry/Entity Type

Supplement

Requirements
Must have
• All information provided in "CREATIVE_BRIEF" file.
Nice to have
Should not have

```html
<!DOCTYPE html>
<html lang="en">
<head>
<meta charset="utf-8">
<title>Bramwell EAA + Energy Label</title>
<link href="https://fonts.googleapis.com/css2?family=Poppins:wght@400;500;600;800&family=Bebas+Neue&display=swap" rel="stylesheet">
<style>
  :root {
    --backdrop: #b2818f;
    --label: #ffffff;
    --accent: #d81452;
    --ink: #141414;
  }
  * { margin: 0; padding: 0; box-sizing: border-box; }
  html, body {
    width: 1200px;
    height: 900px;
    overflow: hidden;
    background: var(--backdrop);
  }
  .canvas {
    position: relative;
    width: 1200px;
    height: 900px;
  }
  .label {
    position: absolute;
    left: 402px;
    top: 300px;
    width: 396px;
    height: 470px;
    background: var(--label);
    font-family: "Poppins", sans-serif;
    color: var(--ink);
    text-align: center;
  }
  .band {
    position: absolute;
    left: 0;
    width: 100%;
    background: var(--accent);
  }
  .band--top { top: 20px; height: 15px; }
  .band--bottom { top: 424px; height: 24px; }
  .brand-name {
    position: absolute;
    top: 108px;
    left: 0;
    width: 100%;
    font-family: "Poppins", sans-serif;
    font-weight: 600;
    font-size: 44px;
    letter-spacing: 4px;
    line-height: 1;
    text-transform: uppercase;
  }
  .product-type {
    position: absolute;
    top: 192px;
    left: 0;
    width: 100%;
    font-weight: 800;
    font-size: 21px;
    line-height: 1;
  }
  .product-sub {
    position: absolute;
    top: 218px;
    left: 0;
    width: 100%;
    font-weight: 400;
    font-size: 20px;
    line-height: 1;
  }
  .flavor {
    position: absolute;
    top: 258px;
    left: 0;
    width: 100%;
    font-family: "Bebas Neue", sans-serif;
    font-size: 42px;
    line-height: 1;
    color: var(--accent);
  }
  .divider {
    position: absolute;
    top: 311px;
    left: 38px;
    width: 314px;
    height: 1px;
    background: var(--ink);
  }
  .tagline {
    position: absolute;
    top: 329px;
    left: 0;
    width: 100%;
    font-weight: 500;
    font-size: 17px;
    line-height: 1.45;
  }
  .net-weight {
    position: absolute;
    top: 396px;
    left: 0;
    width: 100%;
    font-weight: 500;
    font-size: 13.5px;
    line-height: 1;
    letter-spacing: -0.2px;
  }
</style>
</head>
<body>
  <main class="canvas">
    <section class="label">
      <div class="band band--top"></div>
      <h1 class="brand-name">Bramwell</h1>
      <p class="product-type">EAA + Energy</p>
      <p class="product-sub">Amino Blend</p>
      <h2 class="flavor">Raspberry Iced Tea</h2>
      <div class="divider"></div>
      <p class="tagline">For inceased energy and<br>protein synthesis</p>
      <p class="net-weight">NET WT. 360 G ( 12.7 OZ ) | DIETARY SUPPLEMENT</p>
      <div class="band band--bottom"></div>
    </section>
  </main>
</body>
</html>
```